" Atendimento médico em consultório/Clinica para mulheres em geral. A clinica contará com três médicas ginecologistas. Inicialmente somente a Dra. Lívia atenderá. O principal valor da Clinica é com o cuidado com a Mulher através de atendimento individual e cuidadoso através de especialistas nas áreas da ginecologia e Obstetricia. Apesar de possuir atendimento Obstétrico, o mesmo não será o principal foco da clinica. "

```html
<!DOCTYPE html>
<html lang="pt-BR">
<head>
<meta charset="UTF-8">
<title>Ginecologia Serena — Cartão de visita</title>
<link href="https://fonts.googleapis.com/css2?family=Cormorant+Garamond:wght@400;500&family=Oswald:wght@500&family=Open+Sans:wght@400;600&display=swap" rel="stylesheet">
<style>
  :root{
    --bg:#e9e7e8;
    --rose:#e8696f;
    --rose-soft:#f6d3d5;
    --rose-faint:#fbeaeb;
    --white:#ffffff;
    --ink:#2b2b2b;
    --muted:#6b6b6b;
  }
  *{margin:0;padding:0;box-sizing:border-box}
  html,body{width:1200px;height:1200px;overflow:hidden;background:var(--bg)}
  .canvas{position:relative;width:1200px;height:1200px}
  .card{position:absolute;left:160px;width:880px;height:500px;border-radius:40px;overflow:hidden;box-shadow:0 6px 24px rgba(0,0,0,.12)}
  .card--front{top:70px;background:var(--rose);color:var(--white)}
  .card--back{top:630px;background:var(--white)}

  .front-lockup{position:absolute;left:0;right:0;top:120px;text-align:center}
  .brand-dot{width:70px;height:70px;border-radius:50%;border:3px solid var(--white);margin:0 auto 26px}
  .brand-name{font-family:"Cormorant Garamond",serif;font-weight:500;font-size:66px;line-height:1;letter-spacing:1px}
  .doctor-name{font-family:"Cormorant Garamond",serif;font-weight:400;font-size:36px;margin-top:14px;letter-spacing:.5px}

  .back-brand{position:absolute;left:70px;top:150px;display:flex;align-items:center;gap:18px;color:var(--rose-soft);font-family:"Cormorant Garamond",serif;font-weight:500;font-size:40px}
  .back-brand .brand-dot{margin:0;border-color:var(--rose-soft);width:60px;height:60px}
  .back-halo{position:absolute;right:-90px;top:140px;width:420px;height:420px;border-radius:50%;background:var(--rose-faint)}

  .identity{position:absolute;right:50px;top:60px;text-align:right;padding-right:18px;border-right:5px solid var(--rose)}
  .identity .full-name{font-family:"Oswald",sans-serif;font-weight:500;font-size:36px;color:var(--ink);line-height:1.1}
  .identity .role{font-family:"Open Sans",sans-serif;font-size:20px;color:var(--muted)}

  .contacts{position:absolute;right:50px;top:180px;list-style:none;font-family:"Open Sans",sans-serif;font-size:17px;color:var(--muted);text-align:right}
  .contacts li{display:flex;align-items:center;justify-content:flex-end;gap:16px;margin-bottom:16px;line-height:1.3}
  .contact-icon{width:30px;height:30px;flex:none}
  .bottom-band{position:absolute;left:0;right:0;bottom:0;height:28px;background:var(--rose)}
</style>
</head>
<body>
<main class="canvas">

  <section class="card card--front" aria-label="Frente do cartão">
    <div class="front-lockup">
      <div class="brand-dot"></div>
      <h1 class="brand-name">Ginecologia Serena</h1>
      <p class="doctor-name">Dra. Lívia Moraes Tavares</p>
    </div>
  </section>

  <section class="card card--back" aria-label="Verso do cartão">
    <div class="back-halo"></div>
    <div class="back-brand"><div class="brand-dot"></div><span>Ginecologia Serena</span></div>

    <div class="identity">
      <p class="full-name">Nome Completo</p>
      <p class="role">Cargo</p>
    </div>

    <ul class="contacts">
      <li><span>(19) 0000-0000<br>(19) 90000-0000</span>
        <svg class="contact-icon" viewBox="0 0 30 30"><circle cx="15" cy="15" r="14" fill="var(--rose)"/><path d="M10 8h3l1.5 4-2 1.3a9 9 0 0 0 4.2 4.2l1.3-2 4 1.5v3a2 2 0 0 1-2 2A13 13 0 0 1 8 10a2 2 0 0 1 2-2z" fill="#fff"/></svg></li>
      <li><span>Rua das Acácias, 120<br>Centro - São Paulo<br>CEP 00000-000</span>
        <svg class="contact-icon" viewBox="0 0 30 30"><circle cx="15" cy="15" r="14" fill="var(--rose)"/><path d="M15 7a5.5 5.5 0 0 0-5.5 5.5C9.5 17 15 23 15 23s5.5-6 5.5-10.5A5.5 5.5 0 0 0 15 7z" fill="#fff"/><circle cx="15" cy="12.5" r="2" fill="var(--rose)"/></svg></li>
      <li><span>contato@ginecoserena.com.br</span>
        <svg class="contact-icon" viewBox="0 0 30 30"><circle cx="15" cy="15" r="14" fill="var(--rose)"/><rect x="8" y="10" width="14" height="10" rx="1" fill="#fff"/><path d="M8 10.5l7 5 7-5" fill="none" stroke="var(--rose)" stroke-width="1.5"/></svg></li>
      <li><span>Perfil Social</span>
        <svg class="contact-icon" viewBox="0 0 30 30"><circle cx="15" cy="15" r="14" fill="var(--rose)"/><circle cx="15" cy="15" r="5" fill="#fff"/></svg></li>
    </ul>
    <div class="bottom-band"></div>
  </section>

</main>
</body>
</html>
```